High-End audio shop owner needs a business card

I need a personal Business Card for my Audio shop which exists since 1962. We offer high Quality brands, professional Attention and run our own repair-service-department. I look for a design which will be printed on high Quality paper and shall convey trust to the Client that we are very serious. Language is german.

```html
<!DOCTYPE html>
<html lang="de">
<head>
<meta charset="utf-8">
<title>Klangwerk Berger – Visitenkarte</title>
<link rel="stylesheet" href="https://fonts.googleapis.com/css2?family=Roboto:wght@400;500;900&display=swap">
<style>
  :root {
    --orange-light: #f47b20;
    --orange-deep: #ef5523;
    --orange-text: #f05a22;
    --paper: #ffffff;
    --ink: #3c3c3c;
    --ink-soft: #666666;
    --backdrop: #ecebe8;
  }
  * { margin: 0; padding: 0; box-sizing: border-box; }
  html, body { width: 1200px; height: 800px; overflow: hidden; }
  body {
    background: var(--backdrop);
    font-family: "Roboto", Arial, sans-serif;
    position: relative;
  }
  .card {
    position: absolute;
    top: 245px;
    width: 540px;
    height: 310px;
    overflow: hidden;
    box-shadow: 0 6px 18px rgba(0,0,0,0.18);
  }
  .card-front {
    left: 40px;
    background: linear-gradient(160deg, var(--orange-light) 0%, var(--orange-deep) 70%);
  }
  .card-back {
    left: 620px;
    background: var(--paper);
  }
  .sound-area {
    position: absolute;
  }
  .card-front .sound-area {
    left: 0; bottom: 0;
    width: 380px; height: 120px;
    background: linear-gradient(180deg, rgba(255,255,255,0.08) 0%, rgba(255,255,255,0.45) 100%);
  }
  .card-back .sound-area {
    left: 0; bottom: 0;
    width: 540px; height: 40px;
    background: linear-gradient(90deg, rgba(240,90,34,0.55) 0%, var(--orange-text) 100%);
  }
  .card-back .sound-area-rise {
    right: 0; bottom: 40px;
    width: 190px; height: 230px;
    background: linear-gradient(180deg, rgba(240,90,34,0.05) 0%, rgba(240,90,34,0.85) 100%);
  }
  .brand-name {
    position: absolute;
    font-weight: 900;
    font-size: 34px;
    letter-spacing: 0.5px;
    white-space: nowrap;
  }
  .card-front .brand-name { color: var(--paper); right: 26px; top: 78px; }
  .card-back .brand-name { color: var(--orange-text); left: 26px; top: 26px; }
  .holder { position: absolute; left: 48px; top: 100px; }
  .holder-name { color: var(--orange-text); font-size: 17px; font-weight: 500; }
  .holder-role { color: var(--ink-soft); font-size: 12px; margin-top: 2px; }
  .contact-list {
    position: absolute; left: 30px; top: 160px;
    list-style: none;
  }
  .contact-item {
    display: flex; align-items: center; gap: 10px;
    color: var(--ink); font-size: 13px;
    height: 24px;
  }
  .contact-icon { width: 16px; height: 16px; flex: none; }
</style>
</head>
<body>

<section class="card card-front">
  <div class="sound-area" role="img" aria-label="Equalizer-Grafik in Weiß"></div>
  <div class="brand-name">KLANGWERK BERGER</div>
</section>

<section class="card card-back">
  <div class="sound-area" role="img" aria-label="Equalizer-Grafik in Orange"></div>
  <div class="sound-area sound-area-rise" role="img" aria-label="Ansteigende Equalizer-Grafik in Orange"></div>

  <div class="brand-name">KLANGWERK BERGER</div>

  <div class="holder">
    <p class="holder-name">Lukas Brenner</p>
    <p class="holder-role">Geschäftsführer</p>
  </div>

  <ul class="contact-list">
    <li class="contact-item">
      <svg class="contact-icon" viewBox="0 0 16 16" aria-hidden="true"><circle cx="8" cy="8" r="8" fill="#f05a22"/><path d="M5.2 4.2l1.4-.2.8 1.9-1 .8a5 5 0 0 0 2.9 2.9l.8-1 1.9.8-.2 1.4c-3.8.3-6.9-2.8-6.6-6.6z" fill="#fff"/></svg>
      <span>0871 23 45 67</span>
    </li>
    <li class="contact-item">
      <svg class="contact-icon" viewBox="0 0 16 16" aria-hidden="true"><circle cx="8" cy="8" r="8" fill="#f05a22"/><rect x="4" y="5" width="8" height="6" fill="#fff"/><path d="M4 5l4 3.2L12 5" fill="none" stroke="#f05a22" stroke-width="0.9"/></svg>
      <span>info@klangwerkberger.de</span>
    </li>
    <li class="contact-item">
      <svg class="contact-icon" viewBox="0 0 16 16" aria-hidden="true"><circle cx="8" cy="8" r="8" fill="#f05a22"/><circle cx="8" cy="8" r="4" fill="none" stroke="#fff" stroke-width="1"/><path d="M4 8h8M8 4v8" stroke="#fff" stroke-width="0.9"/></svg>
      <span>www.klangwerkberger.de</span>
    </li>
    <li class="contact-item">
      <svg class="contact-icon" viewBox="0 0 16 16" aria-hidden="true"><circle cx="8" cy="8" r="8" fill="#f05a22"/><path d="M8 12.5s-3-3.2-3-5.3a3 3 0 0 1 6 0c0 2.1-3 5.3-3 5.3z" fill="#fff"/><circle cx="8" cy="7.2" r="1.1" fill="#f05a22"/></svg>
      <span>Lindenweg 12, 10115 Berlin</span>
    </li>
  </ul>
</section>

</body>
</html>
```